OPF - Brochure 52 week Curriculum

Oak Path Fellows, Inc. wants to create a distribution Brochure. In the Bible (Matthew 28:18-20)- JESUS said to "TEACH" others what HE has commanded. we want to "PUT IN PRINT"

these 52 lines summarize HIS teachings
we want to use as our Curriculum teaching men ...

incorporate our statements and two main passages of scripture
(see attach pictures of headquarter lobby) to brand uniformity and consistency... we have summarized into 52 groups, but its NOT required to have numbers...
Purpose = obey GOD
Mission = love others
Vision = Development God fearing men globally.

The designer can have freedom in layout and sizing.
we were thinking bi fold , but again... designer has freedom
Please incorporate our colors (white, black, gray) using color wheel provided and our LOGO with website.

```html
<!DOCTYPE html>
<html lang="en">
<head>
<meta charset="utf-8">
<title>Oak Path Fellows – 52 Week Curriculum Brochure</title>
<link rel="stylesheet" href="https://fonts.googleapis.com/css2?family=Alfa+Slab+One&family=Crimson+Text:ital,wght@0,400;0,700;1,400;1,700&display=swap">
<style>
:root{
  --board:#3b2314;
  --paper:#ffffff;
  --ink:#1c1c1c;
  --soft-ink:#3a3a3a;
  --circle:#d3d3d4;
  --grey:#9a9a9a;
  --light-grey:#c9c9c9;
  --rule:#b5b5b5;
}
*{margin:0;padding:0;box-sizing:border-box}
html,body{width:1200px;height:2582px;overflow:hidden;background:var(--board)}
body{position:relative;font-family:"Crimson Text",Georgia,serif;color:var(--ink)}
.spread{position:absolute;width:493px;height:320px;background:var(--paper);overflow:hidden}
.col-left{left:86px}
.col-right{left:619px}
.section-circle{position:absolute;left:46px;top:98px;width:154px;height:154px;border-radius:50%;background:var(--circle);display:flex;align-items:center;justify-content:center;text-align:center;font-size:14px;line-height:1.3;color:var(--soft-ink);padding:10px}
.section-circle.small{font-size:11.5px;line-height:1.25}
.teaching-list{position:absolute;left:267px;width:210px;font-size:7.2px;line-height:1.32;color:var(--soft-ink);list-style:none}
.teaching-list li{position:relative;padding-left:14px;border-left:0.6px solid var(--rule);margin-bottom:8px}
.teaching-list li span.num{position:absolute;left:-16px;width:14px;text-align:right}
.teaching-list.tiny{font-size:5.9px;margin-bottom:0}
.teaching-list.tiny li{margin-bottom:6px}
.teaching-list.large{font-size:9px;line-height:1.25}
.teaching-list.large li{margin-bottom:10px}
.hill-art{position:absolute;left:0;bottom:0;width:112px;height:80px;background:linear-gradient(180deg,rgba(255,255,255,0) 0%,#d8d8d8 55%,#9d9d9d 100%)}
.corner-mark{position:absolute;right:12px;bottom:0;width:46px;height:50px;background:linear-gradient(180deg,#e2e2e2,#cfcfcf)}
.page-no{position:absolute;bottom:11px;font-size:4.5px;color:var(--grey)}
.page-no.left{left:121px}
.page-no.right{left:368px}
/* cover */
.cover-title{position:absolute;left:276px;top:22px;font-family:"Alfa Slab One",Georgia,serif;font-style:italic;font-size:27px;line-height:1.25;color:var(--ink)}
.cover-art{position:absolute;left:246px;top:112px;width:247px;height:208px;background:linear-gradient(180deg,#ffffff 0%,#e4e4e4 45%,#3a3a3a 82%,#111 100%)}
.brand{position:absolute;left:64px;display:flex;flex-direction:column}
.brand-name{font-family:"Crimson Text",Georgia,serif;font-weight:700;font-size:38px;line-height:1;color:var(--ink);letter-spacing:1px}
.brand-url{font-family:"Crimson Text",Georgia,serif;font-weight:700;font-size:6px;color:var(--ink);margin-top:2px}
/* statements */
.statement-bar{position:absolute;left:0;top:35px;width:18px;height:108px;background:var(--circle)}
.statements{position:absolute;left:23px;top:36px;font-size:10px;line-height:1.3}
.statements dt{margin-top:0}
.statements dd{font-style:italic;margin-bottom:11px}
.statements dd.vision{font-weight:700}
.contents{position:absolute;left:282px;top:27px;width:172px}
.contents h2{font-weight:400;font-size:14px;text-align:center;margin-bottom:10px}
.contents ol{list-style:none}
.contents li{display:flex;justify-content:space-between;align-items:center;font-size:4.6px;line-height:1.2;min-height:11.5px;border-left:3px solid var(--ink);border-right:3px solid var(--light-grey);border-bottom:0.6px solid var(--rule);padding:1px 6px;margin-bottom:2.2px}
/* closing */
.closing-art{position:absolute;left:0;bottom:0;width:493px;height:120px;background:linear-gradient(180deg,#ffffff 0%,#d2d2d2 30%,#111 55%,#0a0a0a 100%)}
</style>
</head>
<body>

<!-- Row 1 -->
<section class="spread col-left" style="top:75px">
  <h1 class="cover-title">52 week<br>Curriculum</h1>
  <div class="cover-art" role="img" aria-label="Black and white illustration of a large cross on a grassy hill with trees"></div>
  <div class="brand" style="top:236px">
    <span class="brand-name">OPF</span>
    <span class="brand-url">WWW.OAKPATHFELLOWS.COM</span>
  </div>
</section>

<section class="spread col-right" style="top:75px">
  <div class="section-circle">Living as a Disciple</div>
  <ol class="teaching-list" style="top:22px">
    <li><span class="num">37.</span>Be merciful: Show compassion to others, just as God is merciful. Act with kindness and compassion towards others. Luke 6:36</li>
    <li><span class="num">38.</span>Care for those in distress: Help the hungry, thirsty, strangers, naked, sick, and imprisoned.</li>
    <li><span class="num">39.</span>Recognize your own imperfections and avoid judging others harshly. Matthew 7:1-2, Luke 6:37. Focus on examining your own faults before criticizing others. He taught against judging others, stating that the standard by which you judge will be applied to you (Matthew 7:1-2).</li>
    <li><span class="num">40.</span>Seek God's kingdom first: Make God and his righteousness your highest priority. Prioritize God's reign and right way of living above all else. Found in Matthew 6:33.</li>
    <li><span class="num">41.</span>Abide in JESUS: John 15:4, John 6:35, 40, 47, John 14:27.</li>
    <li><span class="num">42.</span>Follow JESUS: Matthew 4:19, Luke 5:28</li>
  </ol>
  <div class="hill-art" role="img" aria-label="Small cross on a grassy hill"></div>
  <div class="corner-mark" role="img" aria-label="Faint cross decoration"></div>
  <span class="page-no left">16</span><span class="page-no right">17</span>
</section>

<!-- Row 2 -->
<section class="spread col-left" style="top:427px">
  <div class="statement-bar"></div>
  <dl class="statements">
    <dt>Purpose&nbsp; :</dt><dd>obey GOD</dd>
    <dt>Mission&nbsp; :</dt><dd>love others</dd>
    <dt>Vision&nbsp;&nbsp;&nbsp; :</dt><dd class="vision">Development God fearing men globally.</dd>
  </dl>
  <div class="brand" style="top:222px">
    <span class="brand-name">OPF</span>
    <span class="brand-url">WWW.OAKPATHFELLOWS.COM</span>
  </div>
  <nav class="contents">
    <h2>Content</h2>
    <ol>
      <li><span>Regarding God and righteousness</span><span>4</span></li>
      <li><span>Regarding relationships and ethics</span><span>6</span></li>
      <li><span>Regarding personal conduct and Attitudes</span><span>8</span></li>
      <li><span>Prayer</span><span>10</span></li>
      <li><span>Regarding outreach and discipleship</span><span>12</span></li>
      <li><span>Cautions and warnings</span><span>14</span></li>
      <li><span>Living as a Disciple</span><span>16</span></li>
      <li><span>Forgiveness (Jesus Taught about the importance of both<br>receiving and giving forgiveness)</span><span>18</span></li>
      <li><span>Humility and Service</span><span>20</span></li>
      <li><span>Warning against self-righteousness and judgment</span><span>22</span></li>
      <li><span>Money (Jesus taught about using money and<br>possessions responsibly)</span><span>24</span></li>
    </ol>
  </nav>
</section>

<section class="spread col-right" style="top:427px">
  <div class="section-circle small">Forgiveness<br>(Jesus Taught about the importance of both receiving and giving forgiveness)</div>
  <ol class="teaching-list" style="top:105px">
    <li><span class="num">43.</span>Forgive others: Matthew 6:12, 14, Mark 11:25-26, Luke 6:37</li>
    <li><span class="num">44.</span>JESUS emphasized that forgiveness is linked to forgiving others (Matthew 6:14-15)</li>
    <li><span class="num">45.</span>forgiveness should be extended limitlessly to those who repent (Luke 17:3-4; Matthew 18:21-22).</li>
    <li><span class="num">46.</span>forgiveness is also illustrated as the cancellation of debt (Matthew 18:21-35).</li>
  </ol>
  <div class="hill-art" role="img" aria-label="Small cross on a grassy hill"></div>
  <div class="corner-mark" role="img" aria-label="Faint cross decoration"></div>
  <span class="page-no left">18</span><span class="page-no right">19</span>
</section>

<!-- Row 3 -->
<section class="spread col-left" style="top:778px">
  <div class="section-circle">Regarding God<br>and<br>Righteousness</div>
  <ol class="teaching-list" style="top:17px">
    <li><span class="num">1.</span>Repent: Change your mind and actions towards sin, as the Kingdom of Heaven is near. Turn away from sin and toward GOD. Matthew 4:17, Luke 13:3. Repent: This is the call to turn away from sin and embrace the good news of salvation through Jesus Christ. Found in Mark 1:15.</li>
    <li><span class="num">2.</span>Accept the Good News of salvation offered through Jesus.</li>
    <li><span class="num">3.</span>Believe in the Son of God, Jesus Christ: This is essential for salvation and receiving the Holy Spirit. John 6:29, John 14:11</li>
    <li><span class="num">4.</span>Have faith in God, and trust in Jesus as the Son of God.</li>
    <li><span class="num">5.</span>Be born again: John 3:7 Be born again (of water and the Spirit): Experience a spiritual transformation necessary for entrance into God's Kingdom.</li>
    <li><span class="num">6.</span>Give your utmost devotion and affection to God. Love God with all your heart, soul, mind, and strength: Matthew 22:37-38, Mark 12:30, Luke 10:27</li>
    <li><span class="num">7.</span>Honor God's Law: Understand that Jesus did not come to abolish the Law but to fulfill it and to magnify its application in the heart.</li>
  </ol>
  <div class="hill-art" role="img" aria-label="Small cross on a grassy hill"></div>
  <div class="corner-mark" role="img" aria-label="Faint cross decoration"></div>
  <span class="page-no left">4</span><span class="page-no right">5</span>
</section>

<section class="spread col-right" style="top:778px">
  <div class="section-circle small">Warning against<br>self-righteousness<br>and judgment</div>
  <ol class="teaching-list large" style="top:147px">
    <li><span class="num">50.</span>Jesus warned against hypocrisy, particularly the hypocrisy of the Pharisees (Luke 12:1).</li>
  </ol>
  <div class="hill-art" role="img" aria-label="Small cross on a grassy hill"></div>
  <div class="corner-mark" role="img" aria-label="Faint cross decoration"></div>
  <span class="page-no left">22</span><span class="page-no right">23</span>
</section>

<!-- Row 4 -->
<section class="spread col-left" style="top:1129px">
  <div class="section-circle">Regarding<br>relationships<br>and<br>ethics</div>
  <ol class="teaching-list" style="top:17px">
    <li><span class="num">8.</span>Love your Neighbor as yourself: Matthew 22:39, Mark 12:31, Luke 10:27, Leviticus 19:18. Love one another, as I have loved you: Show sacrificial love to fellow believers.</li>
    <li><span class="num">9.</span>The Golden Rule: Treat others as you would want to be treated. (Matthew 7:12). This encapsulates how to treat everyone with respect, kindness, and understanding.</li>
    <li><span class="num">10.</span>Be reconciled to your brother: Seek peace and forgiveness when relationships are broken.</li>
    <li><span class="num">11.</span>Go to those who offend you: Address offenses directly and privately before involving others.</li>
    <li><span class="num">12.</span>Forgive offenders: Extend forgiveness to those who hurt you and forgive often. Forgive others: This is essential for receiving God's forgiveness.</li>
    <li><span class="num">13.</span>Love your enemies and pray for those who persecute you: Matthew 5:44, Luke 6:27-28. Extend compassion even to those who mistreat you.</li>
  </ol>
  <div class="hill-art" role="img" aria-label="Small cross on a grassy hill"></div>
  <div class="corner-mark" role="img" aria-label="Faint cross decoration"></div>
  <span class="page-no left">6</span><span class="page-no right">7</span>
</section>

<section class="spread col-right" style="top:1129px">
  <div class="section-circle">Humility<br>and<br>Service</div>
  <ol class="teaching-list large" style="top:102px">
    <li><span class="num">47.</span>JESUS stated that humility leads to being honored (Luke 14:11; Matthew 23:12)</li>
    <li><span class="num">48.</span>true greatness is found in serving others (Matthew 20:26-28).</li>
    <li><span class="num">49.</span>The Bible also states that God opposes the proud but shows favor to the humble (James 4:6; 1 Peter 5:5).</li>
  </ol>
  <div class="hill-art" role="img" aria-label="Small cross on a grassy hill"></div>
  <div class="corner-mark" role="img" aria-label="Faint cross decoration"></div>
  <span class="page-no left">20</span><span class="page-no right">21</span>
</section>

<!-- Row 5 -->
<section class="spread col-left" style="top:1480px">
  <div class="section-circle">Regarding personal<br>conduct and<br>Attitudes</div>
  <ol class="teaching-list tiny" style="top:18px">
    <li><span class="num">14.</span>Be baptized: Be immersed in water as a symbol of your new life in Christ.</li>
    <li><span class="num">15.</span>Take, eat, and drink in remembrance of Me (Communion/Lord's Supper): Participate in the commemoration of Jesus' sacrifice.</li>
    <li><span class="num">16.</span>Let your light shine before others: Matthew 5:16. Followers are called to live in such a way that their good deeds bring glory to GOD. Demonstrate good works to the world.</li>
    <li><span class="num">17.</span>Care for the less fortunate: Help those in need, such as the hungry, thirsty, strangers, naked, sick, and imprisoned, according to Luke 14:13-14, Matthew 25:31-46.</li>
    <li><span class="num">18.</span>Deny yourself, Take up your cross daily and follow Jesus: This signifies a commitment to discipleship, even in the face of hardship. this teaching is found in Luke 9:23-24; Matthew 16:24-25. Prioritize following Jesus above your own desires and be willing to endure hardship for His sake.</li>
    <li><span class="num">19.</span>Fast: Engage in fasting, but do so for the right reasons and not for outward show.</li>
    <li><span class="num">20.</span>Be wise as serpents and innocent as doves: Matthew 10:16</li>
    <li><span class="num">21.</span>Do not worry about your life or material possessions: Trust God to provide for your needs. Trust God to provide for your needs. Matthew 6:34</li>
    <li><span class="num">22.</span>Lay up treasures in heaven: Focus on building a spiritual inheritance rather than accumulating earthly wealth. Matthew 6:19-21</li>
    <li><span class="num">23.</span>Be a servant: Seek greatness through humble service to others. Serve one another: Matthew 20:25-28</li>
  </ol>
  <div class="hill-art" role="img" aria-label="Small cross on a grassy hill"></div>
  <div class="corner-mark" role="img" aria-label="Faint cross decoration"></div>
  <span class="page-no left">8</span><span class="page-no right">9</span>
</section>

<section class="spread col-right" style="top:1480px">
  <div class="section-circle">Cautions<br>and<br>warnings</div>
  <ol class="teaching-list" style="top:18px">
    <li><span class="num">33.</span>Beware of false prophets: Be discerning and recognize those who may mislead others with false teachings.</li>
    <li><span class="num">34.</span>Beware of leaven (doctrine) of the Pharisees and Sadducees: Avoid hypocrisy and legalism.</li>
    <li><span class="num">35.</span>Be alert and reliant on God's strength to overcome temptation.</li>
    <li><span class="num">36.</span>Do not cast pearls before swine: Use discretion and avoid sharing sacred things with those who may devalue or disrespect them.</li>
  </ol>
  <div class="hill-art" role="img" aria-label="Small cross on a grassy hill"></div>
  <div class="corner-mark" role="img" aria-label="Faint cross decoration"></div>
  <span class="page-no left">14</span><span class="page-no right">15</span>
</section>

<!-- Row 6 -->
<section class="spread col-left" style="top:1831px">
  <div class="section-circle">Prayer</div>
  <ol class="teaching-list" style="top:17px">
    <li><span class="num">24.</span>Jesus provided guidance on prayer, teaching that it should be done in private and with sincerity (Matthew 6:5-8).</li>
    <li><span class="num">25.</span>He also linked prayer to having a forgiving heart (Mark 11:25; Matthew 18:18-20). HE encouraged praying with simple faith and persistence (Luke 11:5-13; Matthew 21:21-22).</li>
    <li><span class="num">26.</span>Pray: Engage in prayer consistently, with sincerity and according to Jesus' example.</li>
    <li><span class="num">27.</span>Prayer for our enemies : Luke 23:24, Matthew 5:44</li>
    <li><span class="num">28.</span>Pray for others : intercession</li>
    <li><span class="num">29.</span>Pray for laborers: Seek God to send workers into the harvest field of souls. Pray for kingdom laborers: Matthew 9:38, Luke 10:2</li>
  </ol>
  <div class="hill-art" role="img" aria-label="Small cross on a grassy hill"></div>
  <div class="corner-mark" role="img" aria-label="Faint cross decoration"></div>
  <span class="page-no left">10</span><span class="page-no right">11</span>
</section>

<section class="spread col-right" style="top:1831px">
  <div class="section-circle small">Money<br>(Jesus taught about using money and possessions responsibly.</div>
  <ol class="teaching-list large" style="top:119px">
    <li><span class="num">51.</span>JESUS advised storing up treasures in Heaven rather than on Earth (Matthew 6:19-21)</li>
    <li><span class="num">52.</span>JESUS stated that it is impossible to serve both God and money (Matthew 6:24).</li>
  </ol>
  <div class="hill-art" role="img" aria-label="Small cross on a grassy hill"></div>
  <div class="corner-mark" role="img" aria-label="Faint cross decoration"></div>
  <span class="page-no left">24</span><span class="page-no right">25</span>
</section>

<!-- Row 7 -->
<section class="spread col-left" style="top:2182px">
  <div class="section-circle">Regarding<br>outreach and<br>discipleship</div>
  <ol class="teaching-list" style="top:17px">
    <li><span class="num">30.</span>Go and make disciples of all nations: Evangelize and teach others to follow Jesus' commands: This is a central command, emphasizing the importance of evangelism and discipleship. Matthew 28:18-20. Teach others to obey all that Jesus commanded: Passing on the teachings of Christ to new believers is a key aspect of discipleship.</li>
    <li><span class="num">31.</span>Feed My Sheep: Care for and nourish the spiritual lives of believers.</li>
    <li><span class="num">32.</span>Receive God's power: Be filled with the Holy Spirit to effectively carry out God's work.</li>
  </ol>
  <div class="hill-art" role="img" aria-label="Small cross on a grassy hill"></div>
  <div class="corner-mark" role="img" aria-label="Faint cross decoration"></div>
  <span class="page-no left">12</span><span class="page-no right">13</span>
</section>

<section class="spread col-right" style="top:2182px">
  <div class="closing-art" role="img" aria-label="Black silhouette of several crosses and trees on a hillside against distant grey mountains"></div>
</section>

</body>
</html>
```